Changing the based bannders and pictures for template

9 Pictures have to be redesign for another product.
Its a template that I bought from the wesite. A website template. I like the pictures but I wanto change the text and product picture in the design.
I ad the pictures of the lighting. This is a example for the products I want. but just to give you a idea.
The font I really like to use the same and the color backgroud. Maybe a little bit different.
To give you a idea of the link of the template :
http://www.layoutvarnik.com/demo/QTR475312/
also a Linke that I also like.
https://www.brumo-kaffi.nl/NL/Pages/Home.aspx

```html
<!DOCTYPE html>
<html lang="en">
<head>
<meta charset="utf-8">
<title>Exclusive European Lighting</title>
<link rel="stylesheet" href="https://fonts.googleapis.com/css2?family=Noto+Serif:wght@400;700&display=swap">
<style>
  :root {
    --teal-deep: #1b9aa6;
    --teal-mid: #3fbcbc;
    --teal-light: #8fdcd6;
    --teal-glow: #b5ebe4;
    --ink: #0d0d0d;
    --product-light: #f3f6f7;
    --product-mid: #dde3e6;
    --product-shade: #b9c4ca;
  }
  * { margin: 0; padding: 0; box-sizing: border-box; }
  html, body {
    width: 1200px;
    height: 551px;
    overflow: hidden;
  }
  .hero-banner {
    position: relative;
    width: 1200px;
    height: 551px;
    overflow: hidden;
  }
  .backdrop {
    position: absolute;
    inset: 0;
    background:
      radial-gradient(ellipse 420px 240px at 880px 230px, var(--teal-glow) 0%, rgba(181,235,228,0) 70%),
      radial-gradient(ellipse 560px 340px at 560px 330px, var(--teal-light) 0%, rgba(143,220,214,0) 75%),
      linear-gradient(115deg, var(--teal-deep) 0%, var(--teal-mid) 42%, var(--teal-light) 68%, var(--teal-mid) 100%);
  }
  .product-visual {
    position: absolute;
    left: 168px;
    top: 46px;
    width: 396px;
    height: 459px;
    border-radius: 14px;
    background: linear-gradient(150deg, var(--product-light) 0%, var(--product-mid) 55%, var(--product-shade) 100%);
    opacity: 0.92;
  }
  .headline {
    position: absolute;
    left: 587px;
    width: 610px;
    top: 212px;
    text-align: center;
    font-family: "Noto Serif", Georgia, serif;
    color: var(--ink);
  }
  .headline-title {
    font-weight: 700;
    font-size: 57px;
    line-height: 1.1;
  }
  .headline-sub {
    margin-top: 8px;
    font-weight: 400;
    font-size: 40px;
    line-height: 1.2;
  }
</style>
</head>
<body>
  <main class="hero-banner">
    <div class="backdrop" role="img" aria-label="Teal low-poly faceted background pattern"></div>
    <div class="product-visual" role="img" aria-label="Product photo: a slim silver laptop shown open at an angle"></div>
    <section class="headline">
      <h1 class="headline-title">Exclusive European</h1>
      <p class="headline-sub">Lighting Brought to the world</p>
    </section>
  </main>
</body>
</html>
```